Real Estate Flyer

Hi - I am assisting a relative to sell a unit. I am looking to have a two page flyer designed (configured as a single page with back to back printing). I have uploaded two samples to give you an idea of the look and feel - one which relates to this property when originally purchased, the other for a different property.
The flyer should includes several key photos on the front along with the wording. The rear should include any secondary photos along with the floor plan.
The flyer should be close to A4 size.

Updates
Hi,
Industry/Entity Type
Real Estate
Look and feel
Each slider illustrates characteristics of the customer's brand and the style your logo design should communicate.

```html
<!DOCTYPE html>
<html lang="en">
<head>
<meta charset="utf-8">
<title>12/40-48 Harbour Lane – Flyer</title>
<link href="https://fonts.googleapis.com/css2?family=Raleway:wght@300;400;600;700&family=Quicksand:wght@300;400;500&display=swap" rel="stylesheet">
<style>
  :root{
    --blue:#1b93c1;
    --blue-light:#a8dce6;
    --red:#e9605a;
    --red-soft:#f6b8b1;
    --ink:#333;
    --paper:#fff;
  }
  *{margin:0;padding:0;box-sizing:border-box}
  html,body{width:1200px;height:849px;overflow:hidden;background:var(--paper)}
  .flyer{position:relative;width:1200px;height:849px;font-family:'Quicksand',sans-serif;color:var(--ink)}
  .photo{position:absolute}
  .hero{left:0;top:0;width:600px;height:382px;background:linear-gradient(160deg,#b8a48a 0%,#c98a64 35%,#e8d8c4 55%,#7fb6dc 75%,#4d8bc4 100%)}
  .hero-tagline{position:absolute;left:405px;top:62px;width:185px;text-align:center;color:#fff}
  .hero-tagline h2{font-family:'Quicksand',sans-serif;font-weight:300;font-size:31px;letter-spacing:1px}
  .hero-tagline p{font-size:12px;line-height:16px;margin-top:12px;letter-spacing:.5px}
  .accent-red-left{position:absolute;left:0;top:352px;width:85px;height:28px;background:var(--red)}
  .thumb{top:318px;height:100px;border:1px solid #fff}
  .thumb-bath{left:90px;width:157px;background:linear-gradient(135deg,#e9eef0,#b7c3c8)}
  .thumb-lounge{left:263px;width:157px;background:linear-gradient(135deg,#ece8e2,#c9c2b8)}
  .thumb-kitchen{left:435px;width:155px;background:linear-gradient(135deg,#f2f2f0,#c8c6c0)}
  .title{position:absolute;right:615px;top:433px;text-align:right}
  .title h1{font-family:'Raleway',sans-serif;font-weight:700;font-size:31px;color:var(--blue);letter-spacing:.3px}
  .title .suburb{font-family:'Raleway',sans-serif;font-weight:400;font-size:19px;color:var(--red);letter-spacing:1.5px;margin-top:2px}
  .intro{position:absolute;left:37px;top:505px;width:290px;font-size:13.5px;line-height:16px}
  .intro em{color:var(--red)}
  .features{position:absolute;left:37px;top:582px;font-size:13.5px;line-height:16px}
  .features h3{font-weight:400;font-size:15px;color:var(--blue);margin-bottom:2px}
  .features ul{list-style:none;padding-left:36px;margin-bottom:10px}
  .callout{position:absolute;left:330px;top:608px;width:250px;text-align:center;color:var(--red);font-size:16px;line-height:19px;letter-spacing:.3px}
  .agent{position:absolute;left:383px;top:762px;font-size:13.5px;line-height:16px}
  .bar{position:absolute;height:10px}
  .bar-blue{left:27px;top:815px;width:424px;background:var(--blue)}
  .bar-red{left:457px;top:815px;width:113px;background:var(--red)}
  .pool{left:626px;top:35px;width:456px;height:363px;background:linear-gradient(180deg,#3b8fd8 0%,#b5623f 30%,#c57a55 55%,#e6d7c2 72%,#2fb8d6 85%,#e6d7c2 100%)}
  .rates{position:absolute;left:627px;top:403px;font-size:11px;line-height:13px;color:var(--blue)}
  .floorplan{position:absolute;left:625px;top:448px;width:340px;height:360px;background:#f3f3f3;border:1px solid #ddd}
  .accent-blue-right{position:absolute;left:1097px;top:37px;width:81px;height:39px;background:var(--blue-light)}
  .side-band{position:absolute;left:1097px;top:88px;width:81px;height:727px;background:linear-gradient(180deg,var(--red-soft) 0%,var(--red) 60%)}
  .side-text{position:absolute;left:1097px;top:815px;width:727px;height:81px;transform-origin:0 0;transform:rotate(-90deg);color:#fff;padding-left:22px}
  .side-text .street{font-family:'Raleway',sans-serif;font-weight:700;font-size:34px;line-height:38px;display:block;margin-top:3px}
  .side-text .suburb{font-family:'Raleway',sans-serif;font-weight:300;font-size:30px;letter-spacing:2px;line-height:34px;display:block}
</style>
</head>
<body>
<div class="flyer">
  <!-- front page -->
  <div class="photo hero" role="img" aria-label="Curved apartment balconies in red brick with views over rooftops to the city"></div>
  <div class="hero-tagline"><h2>Live It Up!</h2><p>Spacious living in a dynamic urban environment</p></div>
  <div class="accent-red-left"></div>
  <div class="photo thumb thumb-bath" role="img" aria-label="Bathroom with vanity and shower"></div>
  <div class="photo thumb thumb-lounge" role="img" aria-label="Empty carpeted lounge room"></div>
  <div class="photo thumb thumb-kitchen" role="img" aria-label="White kitchen with window"></div>

  <div class="title">
    <h1>12/40-48 Harbour Lane</h1>
    <div class="suburb">MARLOW HEIGHTS</div>
  </div>

  <p class="intro">Prominently positioned, this huge <em>“Harbour Lane Apartment”</em> has all the advantages of spacious living in a dynamic urban environment</p>

  <div class="features">
    <h3>This Apartment is Comprised of:</h3>
    <ul>
      <li>2 bedrooms (with built- ins)</li>
      <li>2 bathrooms ( 1 ensuite)</li>
      <li>Spacious lounge/dining room</li>
      <li>Large balcony with magical views</li>
      <li>Internal laundry</li>
    </ul>
    <h3>Enjoy the Resort Style Facilities</h3>
    <ul>
      <li>Swimming pool</li>
      <li>Gym</li>
      <li>Sauna</li>
      <li>Tennis courts</li>
      <li>BBQ area</li>
    </ul>
  </div>

  <p class="callout">Just minutes from the new Marlow Heights Plaza, transport, entertainment and close to city beaches.</p>

  <p class="agent">Hartley &amp; Vane Realty<br>Marlow Heights 5550 1234</p>

  <div class="bar bar-blue"></div>
  <div class="bar bar-red"></div>

  <!-- back page -->
  <div class="photo pool" role="img" aria-label="Apartment building with curved balconies above a blue swimming pool and sun deck"></div>
  <p class="rates">Water Rates: $95.04PQ<br>Council Rates: $646.22PA<br>Strata Rates: $865.05 PA APPROX</p>
  <div class="floorplan" role="img" aria-label="Level five floor plan: two balconies, main bed with ensuite, bed 2, kitchen, living and dining, laundry, plus car space"></div>

  <div class="accent-blue-right"></div>
  <div class="side-band"></div>
  <div class="side-text">
    <span class="street">12/40-48 Harbour Lane</span>
    <span class="suburb">MARLOW HEIGHTS</span>
  </div>
</div>
</body>
</html>
```